Stationery Design Project for Lakemont Kenbu Kai Karate Studio

We Need a Stationery Design for a Karate School Teaching Okinawa Shorin Ryu Karate in Cedarbrook, Vermont, U.S.A.

Target Market(s)

Adults Base Western Speaking aged between 25 and 65 yrs, old that handle household budgets

Industry/Entity Type

School

Requirements
Must have
• Name of business: Lakemont Kenbu Kai Karate Studio
Address: Maplecrest Plaza 38214 US Hwy. 61
Cedarbrook, Vermont. 33812
Phone # : 407-555-0183
email : Lakemontkenbukaistudio@samplemail.net
Logo - attatched

```html
<!DOCTYPE html>
<html lang="en">
<head>
<meta charset="utf-8">
<title>Lakemont Kenbu Kai Karate Studio – Business Card</title>
<link rel="stylesheet" href="https://fonts.googleapis.com/css2?family=Open+Sans:wght@400;700&display=swap">
<style>
  :root {
    --stage: #dcdcdc;
    --card-white: #ffffff;
    --red-deep: #a51c24;
    --red-mid: #d9646b;
    --pink-light: #f6b9bc;
    --ink: #111111;
    --text-grey: #444444;
    --accent-red: #d0202a;
    --watermark: #ededed;
  }
  * { box-sizing: border-box; margin: 0; padding: 0; }
  html, body {
    width: 1200px; height: 913px; overflow: hidden;
    background: var(--stage);
    font-family: "Open Sans", sans-serif;
  }
  .canvas { position: relative; width: 1200px; height: 913px; }

  .card { position: absolute; width: 711px; height: 413px; overflow: hidden; }

  .card--front {
    left: 40px; top: 27px;
    background: radial-gradient(ellipse 62% 78% at 50% 45%, var(--pink-light) 0%, var(--red-mid) 55%, var(--red-deep) 100%);
  }
  .front-brand {
    position: absolute; left: 50%; top: 50%;
    transform: translate(-50%, -50%);
    display: flex; flex-direction: column; align-items: center; gap: 14px;
    color: var(--ink); font-weight: 700; text-align: center;
  }
  .front-brand .brand-dot {
    width: 70px; height: 70px; border-radius: 50%; background: var(--ink);
  }
  .front-brand .brand-name { font-size: 34px; line-height: 1.15; width: 260px; }

  .card--back { left: 433px; top: 459px; background: var(--card-white); }
  .back-brand {
    position: absolute; left: 39px; top: 30px; width: 124px;
    display: flex; flex-direction: column; align-items: center; gap: 10px;
    color: var(--ink); font-weight: 700; text-align: center;
  }
  .back-brand .brand-dot { width: 42px; height: 42px; border-radius: 50%; background: var(--ink); }
  .back-brand .brand-name { font-size: 17px; line-height: 1.15; }

  .watermark {
    position: absolute; left: 565px; top: 200px;
    width: 190px; height: 190px; border-radius: 50%;
    background: var(--watermark);
  }

  .holder { position: absolute; right: 29px; top: 52px; text-align: right; }
  .holder-name { font-size: 36px; color: var(--text-grey); line-height: 1.2; }
  .holder-role { font-size: 36px; color: var(--accent-red); line-height: 1.15; }

  .address {
    position: absolute; left: 33px; top: 260px;
    font-size: 16px; line-height: 24px; color: var(--text-grey); font-style: normal;
  }
  .contact { margin-top: 6px; line-height: 21px; }
  .contact .label { color: var(--accent-red); display: inline-block; width: 20px; }
</style>
</head>
<body>
<main class="canvas">
  <section class="card card--front" aria-label="Card front">
    <div class="front-brand">
      <span class="brand-dot"></span>
      <span class="brand-name">Lakemont Kenbu Kai Karate Studio</span>
    </div>
  </section>

  <section class="card card--back" aria-label="Card back">
    <div class="watermark"></div>
    <div class="back-brand">
      <span class="brand-dot"></span>
      <span class="brand-name">Lakemont Kenbu Kai Karate Studio</span>
    </div>
    <div class="holder">
      <p class="holder-name">Sensei Daniel R. Okada</p>
      <p class="holder-role">Instructor</p>
    </div>
    <address class="address">
      Maplecrest Plaza<br>
      38214 U.S. Hwy 61<br>
      Cedarbrook, Vermont. 33812
      <div class="contact">
        <span class="label">t:</span>407-555-0183<br>
        <span class="label">e:</span>Lakemontkenbukaistudio@samplemail.net
      </div>
    </address>
  </section>
</main>
</body>
</html>
```